Italian Grape Importer needs a Wine Label Design

Uva Dorata provides home winemakers and vineyards with ultra-premium frozen wine grapes direct from Italy. Uva Dorata grapes are highly unique, as they are the only wine grapes available worldwide that are 100% Organic and have the prestigious Italian DOCG certification. We have developed a patented process for flash-freezing wine grapes, right after being picked off of our wines in Italy. This ensures unparalleled quality for the most discerning winemakers around the world.
In addition to its expanding line of premium wine grapes, Uva Dorata also imports high-quality winemaking equipment, such as wine vats, pumps, buckets, etc.
We are looking for a professional graphic designer to create a wine label for us for a wine named "Riverbo": a 50/50 blend of Cabernet Sauvignon and Merlot. In Italian, riverbo means "the encounter/meeting". This wine will be used to promote our grapes to potential customers, both home winemakers and professional wineries and vineyards.
The label should be elegant, clean and modern, yet is approachable to our target consumer (target consumer notes below).
Target Markets:
1. Intermediate and advanced home winemakers looking for high-quality wine grapes (and equipment) that is authentically Italian. These consumers typically are affluent but earthy. They often read Cellarcraft Journal – the #1 magazine for home winemaking.
2. Small vineyards that are looking to supplement their inventory with high-quality imported wine grapes.
The label should measure 4" x 6" and include the following information:
Brand Name: Uva Dorata
Uva Dorata Logo
Wine Name: Riverbo
Blend: 50/50 Cabernet Sauvignon/Merlot
Organic, DOCG, Tuscany
Look and Feel:
• Elegant
• Serious
• Modern/Traditional
• Personable but Professional
• Gender Neutral
• Upmarket
I have attached example images to demonstrate the feel that we are looking for. These are just a possible starting point. The expectation is that the label would be professional/polished.
Note:
I've added some wine labels that we've come across that have the feel that we would like for our wine label. We want it to be clean and elegant - think valdren kross, KTR, Lavelle & Boiron. One possible color to be used is Pantone 19-2524 (Dark Purple), or Pantone 19-2428 (Magenta Purple) with silver/grey/black

```html
<!DOCTYPE html>
<html lang="en">
<head>
<meta charset="utf-8">
<title>Uva Dorata – Riverbo Label</title>
<link rel="stylesheet" href="https://fonts.googleapis.com/css2?family=Cinzel:wght@400&family=Parisienne&display=swap">
<style>
  :root {
    --stage: #675a6a;
    --label-mauve: #6a4d63;
    --label-plum: #431c52;
    --silver: #dcd6de;
    --silver-soft: #bfb6c2;
    --art-dark: #050306;
    --art-deep: #1c1222;
  }
  * { margin: 0; padding: 0; box-sizing: border-box; }
  html, body { width: 1200px; height: 1060px; overflow: hidden; }
  body { background: var(--stage); position: relative; }

  .label {
    position: absolute;
    width: 312px;
    height: 466px;
    transform-origin: top left;
    transform: scale(1.45);
    color: var(--silver);
    font-family: "Cinzel", serif;
    text-align: center;
  }
  .label--mauve { left: 112px; top: 192px; background: var(--label-mauve); }
  .label--plum  { left: 636px; top: 192px; background: var(--label-plum); }

  .brand-mark { position: absolute; top: 16px; left: 0; width: 100%; }
  .brand-mark__dot {
    display: block; width: 14px; height: 14px; margin: 0 auto 4px;
    border-radius: 50%; background: var(--silver);
  }
  .brand-mark__name { font-size: 5px; letter-spacing: 0.5px; }

  .wordmark {
    position: absolute; left: 0; width: 100%;
    font-family: "Parisienne", cursive;
    font-size: 36px; line-height: 1;
    color: var(--silver);
  }
  .label--mauve .wordmark { top: 78px; }
  .label--plum .wordmark { top: 74px; font-size: 32px; }

  .frame { position: absolute; }
  .frame__glow {
    position: absolute;
    background: linear-gradient(135deg, #7a3f6a, #4d6a3a 40%, #6a3f7a 70%, #3f5a8a);
    opacity: 0.75;
  }
  .frame__art {
    position: absolute;
    background: linear-gradient(160deg, var(--art-deep), var(--art-dark));
  }
  .frame__line { position: absolute; background: var(--silver); }

  .label--mauve .frame { left: 47px; top: 120px; width: 215px; height: 215px; }
  .label--mauve .frame__glow { inset: 0; }
  .label--mauve .frame__art { left: 17px; top: 18px; width: 183px; height: 180px; }

  .label--plum .frame { left: 66px; top: 126px; width: 180px; height: 180px; }
  .label--plum .frame__glow { inset: 0; }
  .label--plum .frame__art { left: 14px; top: 14px; width: 152px; height: 152px; }

  .wine-name { position: absolute; left: 0; width: 100%; line-height: 1; }
  .label--mauve .wine-name { top: 332px; font-size: 18px; letter-spacing: 0.5px; }
  .label--plum .wine-name { top: 314px; font-size: 17px; letter-spacing: 6px; }

  .blend { position: absolute; left: 0; width: 100%; font-size: 10px; line-height: 1; }
  .label--mauve .blend { top: 362px; }
  .label--plum .blend { top: 377px; font-size: 9.5px; }

  .vintage { position: absolute; left: 0; width: 100%; font-size: 7px; letter-spacing: 3px; line-height: 1; }
  .label--mauve .vintage { top: 383px; }
  .label--plum .vintage { top: 398px; }

  .origin {
    position: absolute; left: 0; width: 100%; top: 448px;
    font-size: 6px; line-height: 1; color: var(--silver-soft);
  }
</style>
</head>
<body>

<section class="label label--mauve">
  <div class="brand-mark">
    <span class="brand-mark__dot"></span>
    <div class="brand-mark__name">Uva Dorata</div>
  </div>
  <div class="wordmark">Uva Dorata</div>
  <div class="frame">
    <div class="frame__glow"></div>
    <div class="frame__art" role="img" aria-label="Artwork: rainbow petal swirl on black"></div>
    <div class="frame__line" style="right:0; top:0; width:1px; height:60px;"></div>
    <div class="frame__line" style="left:160px; top:0; width:55px; height:1px;"></div>
    <div class="frame__line" style="left:0; top:150px; width:1px; height:65px;"></div>
    <div class="frame__line" style="left:0; top:214px; width:40px; height:1px;"></div>
  </div>
  <div class="wine-name">RIVERBO</div>
  <div class="blend">50/50 Cabernet Sauvignon/Merlot</div>
  <div class="vintage">2014</div>
  <div class="origin">ORGANIC, DOCG, TUSCANY</div>
</section>

<section class="label label--plum">
  <div class="brand-mark">
    <span class="brand-mark__dot"></span>
    <div class="brand-mark__name">Uva Dorata</div>
  </div>
  <div class="wordmark">Uva Dorata</div>
  <div class="frame">
    <div class="frame__glow"></div>
    <div class="frame__art" role="img" aria-label="Artwork: rainbow petal swirl on black"></div>
    <div class="frame__line" style="right:0; top:0; width:1px; height:180px;"></div>
    <div class="frame__line" style="left:140px; top:0; width:40px; height:1px;"></div>
    <div class="frame__line" style="left:0; top:100px; width:1px; height:80px;"></div>
    <div class="frame__line" style="left:0; top:179px; width:180px; height:1px;"></div>
  </div>
  <div class="wine-name">RIVERBO</div>
  <div class="blend">50/50 Cabernet Sauvignon/Merlot</div>
  <div class="vintage">2014</div>
  <div class="origin">ORGANIC, DOCG, TUSCANY</div>
</section>

</body>
</html>
```